Creative Flyer Design Project

I want to create a flyer. I have attached wireframe (wireframe.png) of flyer which gives you much needed idea regarding flyer content. I have attached few images from our portfolio which can be used while designing a flyer.

I would like you to show me the extreme creativity and capability in delivering world class flyer design.

No heavy graphics needed. I want extremely clean and professional flyer using icons, colors and highlighted text/headings.

I will be requiring multiple formats of flyer such as .ai/.png/.psd/pdf.

Size of flyer: Standard A4 size OR Height is at discretion of designer. The width must be below 780 px.

Fonts to be used: Web 2.0 fonts needed. Must drive message clearly.

*** Long term association oppurtunity exists for the right creative designers for direct work

Business owners

Work

• Cartoonish or cheap graphics

```html
<!DOCTYPE html>
<html lang="en">
<head>
<meta charset="utf-8">
<title>Custom Graphic Design Services Flyer</title>
<link rel="stylesheet" href="https://fonts.googleapis.com/css2?family=Arimo:wght@400;700&family=Cinzel:wght@400;700&display=swap">
<style>
:root{
  --ink-dark:#161718;
  --ink-mid:#2a2c2e;
  --paper:#f4f5f5;
  --paper-shade:#dde1e3;
  --text-dark:#333638;
  --text-light:#e8e8e8;
  --blue:#2b8fca;
  --blue-deep:#1c6fa3;
  --orange:#e4501f;
  --orange-deep:#c53a12;
  --red:#b5161e;
  --red-deep:#8d0f15;
  --amber:#f6a01a;
  --sky:#2ea3da;
  --teal:#2b8e98;
  --promo:#d7231c;
  --link:#4aa3ec;
  --silver:#c9cccf;
}
*{margin:0;padding:0;box-sizing:border-box}
html,body{width:1200px;height:2630px;overflow:hidden}
body{position:relative;font-family:"Arimo",Arial,sans-serif;background:var(--ink-dark);color:var(--text-light)}
.abs{position:absolute}

/* header */
.hero{left:0;top:0;width:1200px;height:1362px;background:radial-gradient(ellipse at 50% 0%,#3a3c3f 0%,#202123 45%,var(--ink-dark) 100%)}
.hero-arc{left:0;top:0}
.kicker{left:0;top:22px;width:1200px;text-align:center;font-size:36px;color:#fff}
.headline{left:0;top:58px;width:1200px;text-align:center;font-family:"Cinzel",Georgia,serif;font-weight:700;font-size:78px;letter-spacing:1px;color:#fff;font-variant:small-caps}
.subline{left:0;top:160px;width:1200px;text-align:center;font-size:36px;color:#fff}

/* services panel */
.panel-wave{left:0;top:320px}
.tab{color:#fff;font-weight:700;display:flex;align-items:center;justify-content:center;box-shadow:0 3px 6px rgba(0,0,0,.35)}
.tab-identity{left:38px;top:372px;width:300px;height:52px;font-size:26px;background:linear-gradient(#48a6dc,var(--blue-deep));justify-content:flex-start;padding-left:34px}
.tab-print{left:288px;top:460px;width:488px;height:54px;font-size:27px;background:linear-gradient(#f0673a,var(--orange-deep))}
.tab-web{left:688px;top:580px;width:475px;height:62px;font-size:27px;background:linear-gradient(#cf2a30,var(--red-deep))}
.card{background:#fff;box-shadow:0 2px 8px rgba(0,0,0,.18);color:var(--text-dark);font-size:15px}
.card ul{list-style:none}
.card li{position:relative;padding-left:22px;height:30px;line-height:30px;white-space:nowrap}
.card li::before{content:"";position:absolute;left:4px;top:12px;width:7px;height:7px;border-radius:50%}
.card-identity{left:50px;top:424px;width:262px;height:240px;padding:12px 14px;background:rgba(255,255,255,.85)}
.card-identity li{height:31px;line-height:31px}
.card-identity li::before{background:var(--blue)}
.card-print{left:312px;top:514px;width:464px;height:300px;padding:10px 14px;display:flex;gap:10px}
.card-print ul{flex:1}
.card-print li::before{background:var(--orange)}
.card-web{left:712px;top:642px;width:450px;height:212px;padding:12px 14px;display:flex;gap:8px}
.card-web ul{flex:1}
.card-web li::before{background:var(--red)}

/* benefits & process */
.block-title{color:var(--amber);font-weight:700;font-size:28px;text-align:center;line-height:36px}
.benefits-title{left:120px;top:912px;width:500px}
.benefits{left:150px;top:1010px;width:500px;list-style:none;font-size:15px;color:var(--text-light)}
.benefits li{position:relative;padding-left:34px;line-height:20px;margin-bottom:20px}
.benefits li::before{content:"";position:absolute;left:4px;top:6px;width:8px;height:8px;border-radius:50%;background:#fff}
.process-title{left:660px;top:925px;width:440px}
.process{left:668px;top:1030px;width:520px;list-style:none;font-size:14px;color:var(--text-light)}
.process li{height:34px;line-height:18px;position:relative}
.process li:not(:last-child)::after{content:"";position:absolute;left:118px;top:21px;border-left:4px solid transparent;border-right:4px solid transparent;border-top:7px solid #bbb}
.formats{left:668px;top:1300px;display:flex;gap:14px}
.format{width:40px;height:46px;border-radius:4px;font-size:11px;font-weight:700;color:#fff;display:flex;align-items:flex-end;justify-content:center;padding-bottom:4px}

/* showcase */
.showcase{left:0;top:1340px;width:1200px;height:700px}
.showcase-art{left:75px;top:1420px;width:1075px;height:390px;border-radius:30px;background:radial-gradient(ellipse at 55% 50%,#c9d8e6 0%,#e3e9ee 55%,rgba(255,255,255,0) 80%)}
.partner-line{left:0;top:1838px;width:1200px;text-align:center;font-size:37px;font-weight:700;color:var(--sky)}

/* contact */
.contact{left:0;top:1960px;width:1200px;height:480px}
.seal{left:150px;top:2040px;width:200px;height:200px;border-radius:50%;background:radial-gradient(circle at 40% 35%,#f4f5f6,var(--silver) 60%,#8e9397);box-shadow:0 4px 10px rgba(0,0,0,.3)}
.call{left:463px;top:2135px;display:flex;align-items:center;gap:14px;font-size:31px;color:var(--text-dark)}
.contact-row{display:flex;align-items:center;gap:12px;font-size:17px;color:var(--text-dark)}
.dot{width:28px;height:28px;border-radius:50%}
.c1{left:410px;top:2210px}.c2{left:410px;top:2250px}.c3{left:835px;top:2202px}.c4{left:835px;top:2242px}

/* promo & footer */
.promo{left:38px;top:2368px;width:1125px;height:64px;background:var(--promo);border:2px solid #ef6b60;display:flex;align-items:center;justify-content:space-between;padding:0 24px;font-size:29px;color:#fff}
.promo strong{font-size:33px;font-weight:400}
.footer{left:0;top:2436px;width:1200px;height:194px;background:var(--ink-dark)}
.site-logo{left:72px;top:2502px;font-family:"Cinzel",Georgia,serif;font-size:40px;color:#fff;font-variant:small-caps}
.visit{left:365px;top:2506px;font-size:33px;color:var(--link);text-decoration:underline}
</style>
</head>
<body>

<section class="abs hero"></section>
<svg class="abs hero-arc" width="1200" height="300" viewBox="0 0 1200 300" aria-hidden="true">
  <path d="M-40 140 Q600 -30 1240 140" fill="none" stroke="#4a4d51" stroke-width="2"/>
</svg>
<p class="abs kicker">100% Custom graphic designs at the</p>
<h1 class="abs headline">Most affordable prices</h1>
<p class="abs subline">Our services are available in 36 design categories</p>

<svg class="abs panel-wave" width="1200" height="620" viewBox="0 0 1200 620" aria-hidden="true">
  <defs>
    <linearGradient id="panelFill" x1="0" y1="0" x2="0" y2="1">
      <stop offset="0" stop-color="#fbfbfb"/><stop offset="1" stop-color="#d9dee0"/>
    </linearGradient>
  </defs>
  <path d="M0 40 C350 10 800 0 1200 60 L1200 480 C950 520 700 580 420 540 C260 518 120 530 0 570 Z" fill="url(#panelFill)"/>
  <path d="M0 548 C160 505 320 505 470 545 C320 528 160 545 0 600 Z" fill="var(--orange)"/>
  <path d="M0 575 C140 545 260 540 380 552 C250 552 120 575 0 612 Z" fill="var(--red-deep)"/>
  <path d="M640 568 C850 540 1030 480 1200 440 L1200 520 C1020 552 850 580 640 568 Z" fill="var(--blue)"/>
</svg>

<div class="abs tab tab-identity">Corporate identity</div>
<div class="abs card card-identity">
  <ul>
    <li>Logo design</li><li>Stationery design</li><li>Business card design</li><li>Envelope design</li>
    <li>Letterhead design</li><li>Presentation folder design</li><li>Slide deck template design</li>
  </ul>
</div>

<div class="abs tab tab-print">Graphics/Print design</div>
<div class="abs card card-print">
  <ul>
    <li>T-shirt design</li><li>Brochure design</li><li>Poster design</li><li>Postcard design</li><li>Flyer design</li>
    <li>Book cover design</li><li>Label / Sticker design</li><li>CD cover design</li><li>Trade show display</li>
  </ul>
  <ul>
    <li>Signage design</li><li>Newspaper ad design</li><li>Greeting card /</li><li>Invitation design</li><li>Packaging design</li>
    <li>Vehicle wrap design</li><li>Shopping bag design</li><li>Door hanger design</li><li>Certificate design</li>
  </ul>
</div>

<div class="abs tab tab-web">Web design</div>
<div class="abs card card-web">
  <ul>
    <li>Landing page design</li><li>Web page design</li><li>Ecommerce web design</li><li>Blog design</li>
    <li>CMS website design</li><li>Newsletter design</li>
  </ul>
  <ul>
    <li>Banner ad design</li><li>Chatterly page design</li><li>Chirpnet page design</li><li>Vidstream page design</li><li>Myzone page design</li>
  </ul>
</div>

<h2 class="abs block-title benefits-title">Benefits you get by dealing with<br>aaaaaaaaaaaaaa.com</h2>
<ul class="abs benefits">
  <li>Creatively crafted functional designs</li>
  <li>Highly affordable pricing</li>
  <li>Multiple variations of designs submitted</li>
  <li>Variations open to revisions</li>
  <li>Guaranteed 48 hours delivery</li>
  <li>30000+ ready designs also available, all open for 100%<br>customization at no extra cost</li>
</ul>

<h2 class="abs block-title process-title">Our design process</h2>
<ol class="abs process">
  <li>Careful analysis of your individual &amp; business needs</li>
  <li>Creation of rough hand drawn sketches</li>
  <li>Analyzing sketches &amp; shortlisting them</li>
  <li>Conversion of shortlisted hand drawn sketches to digital formats</li>
  <li>Submission of multiple variations of designs to choose from</li>
  <li>Feedback/suggestions rounds to give final shape to your design</li>
  <li>Delivery of design in multiple digital formats</li>
</ol>
<div class="abs formats">
  <span class="format" style="background:#2c6fb5">PSD</span>
  <span class="format" style="background:#3b8fd1">PNG</span>
  <span class="format" style="background:#4aa6dc">JPG</span>
  <span class="format" style="background:#2e94c7">EPS</span>
  <span class="format" style="background:#5aaa2e">CDR</span>
  <span class="format" style="background:#8a9096">TIF</span>
  <span class="format" style="background:#c9282d">PDF</span>
  <span class="format" style="background:#e07a12">AI</span>
</div>

<svg class="abs showcase" width="1200" height="700" viewBox="0 0 1200 700" aria-hidden="true">
  <path d="M0 40 C300 0 800 10 1200 30 L1200 700 L0 700 Z" fill="#ffffff"/>
</svg>
<div class="abs showcase-art" role="img" aria-label="Collage of portfolio work: printed cards, brochures, software boxes, discs, product labels and website screenshots"></div>
<p class="abs partner-line">Preferred partner for 5000+ individuals &amp; businesses</p>

<svg class="abs contact" width="1200" height="480" viewBox="0 0 1200 480" aria-hidden="true">
  <defs>
    <linearGradient id="greyFill" x1="0" y1="0" x2="0" y2="1">
      <stop offset="0" stop-color="#f2f3f3"/><stop offset="1" stop-color="#d5d8da"/>
    </linearGradient>
  </defs>
  <path d="M0 60 C400 130 800 20 1200 0 L1200 480 L0 480 Z" fill="url(#greyFill)"/>
  <path d="M0 40 C400 120 800 10 1200 -10 L1200 70 C800 80 400 150 0 90 Z" fill="var(--teal)" opacity=".9"/>
  <path d="M0 88 C400 150 800 78 1200 66 L1200 90 C800 100 400 170 0 110 Z" fill="#8fc9cf" opacity=".6"/>
</svg>
<div class="abs seal" role="img" aria-label="Plain silver guarantee seal"></div>
<div class="abs call">
  <svg width="36" height="36" viewBox="0 0 36 36" aria-hidden="true">
    <rect width="36" height="36" rx="6" fill="var(--teal)"/>
    <path d="M12 8 l5 5 -3 3 q2 4 6 6 l3 -3 5 5 -3 4 q-10 -1 -17 -13 z" fill="#fff"/>
  </svg>
  <span>Call us now: +11 88888 99999</span>
</div>
<div class="abs contact-row c1"><span class="dot" style="background:#5aa93a"></span>xxxxxxxxxxxxxxxxxx</div>
<div class="abs contact-row c2"><span class="dot" style="background:#2f7fc4"></span>info@xxxxxxxxxxxx.com</div>
<div class="abs contact-row c3"><span class="dot" style="background:#2ea3da"></span>yyyyyyyyyyyy</div>
<div class="abs contact-row c4"><span class="dot" style="background:#7a3fa0"></span>zzzzzzzzzzz</div>

<div class="abs footer"></div>
<div class="abs promo"><span>21% Special discount for our insider members</span><strong>Use » zzzzzzz2013</strong></div>
<div class="abs site-logo">Site logo</div>
<div class="abs visit">Visit www.aaaaaaaaaaaaaa.com today!</div>

</body>
</html>
```